Bring me business with this creative business card

Design my new business card. I am looking for something different with an impact. People will take a look at this card & they will 1- see how different & creative I am, 2-understand what I do 3- Call me to meet me!

I make videos with a message, testimonials. I am dynamic, fun, creative & human. My new website is in construction but in the meantime you can check this old one: brightpath.ca & another one Ferncove.com & ferncove facebook page.
I make videos. sometimes with a cameraman, sometimes with my phone. As an ex Public Relations agent, the message is the most important thing for me. I want to make my clients shine! When they start with me they often remind me of a lamb, when I finish coaching them they are powerful like LIONS! That's why I need a powerful business card!

Target Market(s)

Entrepreneurs, solo entrepreneurs, small & medium companies & start ups. People i will meet while networking. People that need videos on their website & social Networks to get attention, to be visible. men & women. From 35 to 49 years old.
I am an ex Public relations agent. I used to send clients in traditional medias, now with videos they have more chances to be seen on google the new media. I do videos of the president, his team, his loyal clients saying how great the company is & expert videos like series so people can be seen for example every 1 st of every month with a short 2 minute video. Also with my 20 years in marketing & communications I can coach & give tips to anybody who needs it.
Target: anybody who would like my old website brightpath.ca & I also have another website but it will be off line soon: ferncove.com could give you ideas.

Industry/Entity Type

Communications

Contact Information for Business Card

I am in Montreal,So the business cards have to be the usual size like we have in Montreal: 9 cm x 5 cm
Details:My text: Martine Gaudreau Communication Coach/Story Chief. "Creating Videos as unique as you" off: 514-555-3047 cell: 514-555-6182. ferncove.com
martine@ferncove.com logo facebook, youtube, instagram

Colors
f37122

Requirements
Must have
• Dynamic, happy. Orange. Be creative in the look but NOT the shape of the card. Easy to read. Big enough to read.
Should not have
• No funny shapes: no round, no square, just the usual. I love creative but NOT on shape.

```html
<!DOCTYPE html>
<html lang="en">
<head>
<meta charset="utf-8">
<title>Ferncove – Business Card</title>
<link rel="stylesheet" href="https://fonts.googleapis.com/css2?family=Cinzel:wght@700&family=Montserrat:wght@400;500&display=swap">
<style>
  :root {
    --bg: #2a2a2c;
    --ink: #0b0a0a;
    --paper: #ffffff;
    --orange: #f37122;
    --amber: #f7a21b;
    --grey: #5c5c5c;
  }
  * { box-sizing: border-box; margin: 0; padding: 0; }
  html, body { width: 1200px; height: 900px; overflow: hidden; background: var(--bg); }
  .stage { position: relative; width: 1200px; height: 900px; }

  .card { position: absolute; left: 240px; width: 720px; height: 400px; overflow: hidden; }

  /* Front */
  .card-front { top: 40px; background: var(--ink); }
  .brand { position: absolute; inset: 0; display: flex; flex-direction: column; align-items: center; justify-content: center; gap: 14px; }
  .brand-dot { width: 110px; height: 110px; border-radius: 50%; background: var(--orange); }
  .brand-name { font-family: "Cinzel", serif; font-weight: 700; font-size: 54px; letter-spacing: 4px; color: var(--orange); line-height: 1; }
  .brand-tagline { display: flex; align-items: center; gap: 10px; font-family: "Montserrat", sans-serif; font-weight: 500; font-size: 15px; letter-spacing: 1px; color: var(--amber); }
  .brand-tagline::before, .brand-tagline::after { content: ""; width: 40px; height: 1px; background: var(--amber); }

  /* Back */
  .card-back { top: 460px; background: var(--paper); font-family: "Montserrat", sans-serif; }
  .name-band { position: absolute; left: 0; top: 52px; width: 640px; height: 110px; background: var(--ink); clip-path: polygon(0 0, 100% 20%, 100% 100%, 0 78%); }
  .name-block { position: absolute; left: 30px; top: 66px; color: var(--orange); text-transform: uppercase; }
  .name-block .person { font-size: 24px; font-weight: 500; letter-spacing: 1px; }
  .name-block .role { font-size: 18px; letter-spacing: 1px; margin-top: 2px; }
  .band-dot { position: absolute; left: 595px; top: 65px; width: 112px; height: 112px; border-radius: 50%; background: var(--orange); }

  .contacts { position: absolute; left: 56px; top: 216px; list-style: none; color: var(--grey); font-size: 21px; letter-spacing: 1px; line-height: 28px; }
  .contacts li { display: flex; align-items: center; gap: 14px; }
  .contacts svg { width: 16px; height: 16px; flex: none; }

  .social { position: absolute; left: 50px; top: 318px; display: flex; align-items: center; gap: 8px; }
  .social-dot { width: 26px; height: 26px; border-radius: 50%; background: var(--orange); }
  .social-handle { margin-left: 12px; font-size: 21px; color: #222; letter-spacing: 0.5px; }

  .site { position: absolute; right: 30px; bottom: 26px; font-size: 21px; color: var(--grey); letter-spacing: 0.5px; }
  .site .accent { color: var(--amber); }
  .site-bar { position: absolute; right: 30px; bottom: 0; width: 230px; height: 16px; background: var(--orange); }
</style>
</head>
<body>
<main class="stage">
  <section class="card card-front" aria-label="Card front">
    <div class="brand">
      <div class="brand-dot"></div>
      <div class="brand-name">FERNCOVE</div>
      <div class="brand-tagline">1 CLIP 1 STORY</div>
    </div>
  </section>

  <section class="card card-back" aria-label="Card back">
    <div class="name-band"></div>
    <div class="name-block">
      <div class="person">Martine G.</div>
      <div class="role">Communication Coach/Story Chief</div>
    </div>
    <div class="band-dot"></div>

    <ul class="contacts">
      <li><svg viewBox="0 0 16 16"><rect x="4" y="1" width="8" height="14" rx="1.5" fill="none" stroke="#f37122" stroke-width="1.6"/></svg>514-555-3047</li>
      <li><svg viewBox="0 0 16 16"><path d="M4 2c-2 1-2 4 0 7s5 6 8 5l1-2-3-2-1 1c-1-.5-3-2.5-3.5-3.5l1-1L5 2z" fill="#f37122"/></svg>514-555-6182</li>
      <li><svg viewBox="0 0 16 16"><rect x="1.5" y="3.5" width="13" height="9" fill="none" stroke="#f37122" stroke-width="1.4"/><path d="M1.5 3.5 8 9l6.5-5.5" fill="none" stroke="#f37122" stroke-width="1.4"/></svg>martine@ferncove.com</li>
    </ul>

    <div class="social">
      <span class="social-dot"></span>
      <span class="social-dot"></span>
      <span class="social-dot"></span>
      <span class="social-handle">/ferncove.com</span>
    </div>

    <div class="site">www.<span class="accent">ferncove</span>.com</div>
    <div class="site-bar"></div>
  </section>
</main>
</body>
</html>
```